Corvel Ridge New Website Design

We just changed our logo (thank you PlanHarbor) and company name change from Corvel Ridge Machining to Corvel Ridge Manufacturing. We do CNC Swiss screw machining and multi-axis machines. We make parts for many industries. We make large quantity production parts as well small R&D quantities. You can look at our current (outdated) website: http://www.corvelridgemachining.example to see what we do. We would like a WordPress site, including contact form for "request for quote" . We would also like it to be mobile friendly, and the ability to maintain it ourselves after it is finished I have included our new logo and fonts for references. We would like our site to convey the feeling of precision, capability, and trust worthiness with a very modern look. The new website address is www.corvelridge-mfg.example

Coding

Coded - Design and coding required

Number of Pages Required

5+ page

Font styles to use
Serif
Sans Serif
Other font styles liked:
• fronts included, not sure if they work

Colors

Designer to choose colors to be used in the design.

Requirements
Must have
• Contact Info, request for quote field

```html
<!DOCTYPE html>
<html lang="en">
<head>
<meta charset="utf-8">
<title>Corvel Ridge Manufacturing</title>
<link rel="stylesheet" href="https://fonts.googleapis.com/css2?family=Arimo:wght@700&family=Raleway:wght@400;500;600&display=swap">
<style>
:root{
  --blue:#1d4486;
  --blue-box:rgba(42,84,170,.85);
  --btn:#4a6aa8;
  --btn-edge:#1d4486;
  --ink:#111;
  --text:#777;
  --head:#333;
  --link:#1d4486;
  --footer:#333a47;
  --footer-bottom:#2c323e;
  --panel:#f5f5f5;
  --white:#fff;
}
*{box-sizing:border-box;margin:0;padding:0}
html,body{width:1200px;height:2865px;overflow:hidden}
body{position:relative;background:var(--white);font-family:"Raleway",sans-serif;color:var(--text)}
.abs{position:absolute}
/* header */
.hero{left:0;top:0;width:1200px;height:676px;background:linear-gradient(120deg,#6f7a86 0%,#a9b3be 30%,#c9ced4 50%,#8f99a5 75%,#5b6571 100%)}
.site-header{left:0;top:0;width:1200px;height:105px;background:rgba(40,44,52,.75)}
.brand{display:flex;align-items:center;gap:10px;color:var(--white);font-family:"Raleway",sans-serif;font-weight:600;font-size:22px;letter-spacing:1px}
.brand-dot{width:22px;height:22px;border-radius:50%;border:3px solid var(--white)}
.brand small{display:block}
.nav{top:43px;left:0;width:1200px;color:var(--white);font-size:15px;font-weight:500}
.nav span{position:absolute;white-space:nowrap}
.nav .active{font-weight:600}
.caret{left:435px;top:67px}
.search{left:1102px;top:41px}
.hero-box{left:277px;top:260px;width:646px;height:260px;background:var(--blue-box);display:flex;align-items:center;justify-content:center;text-align:center}
.hero-box h1{font-family:"Arimo",sans-serif;font-size:49px;line-height:62px;color:var(--white);text-transform:uppercase}
/* welcome */
.section-title{font-family:"Arimo",sans-serif;font-size:38px;color:var(--ink);text-align:center;width:1200px;left:0}
.welcome-text{left:240px;top:800px;width:720px;text-align:center;font-size:14.5px;line-height:26px}
.btn{width:151px;height:52px;color:var(--white);font-size:16px;display:flex;align-items:center;justify-content:center;background:var(--btn);clip-path:polygon(0 0,100% 0,100% 100%,0 100%)}
.btn::before,.btn::after{content:"";position:absolute;top:0;width:16px;height:100%;background:var(--btn-edge)}
.btn::before{left:0;clip-path:polygon(0 0,100% 0,0 100%)}
.btn::after{right:0;clip-path:polygon(100% 0,100% 100%,0 100%)}
/* industries */
.industries{left:0;top:1093px;width:1200px;height:437px;background:var(--blue)}
.industries-photo{left:0;top:1093px;width:1200px;height:437px;background:linear-gradient(135deg,#c8cfd6,#8e99a6 45%,#b9443c 80%,#d9dde2);clip-path:polygon(639px 0,1200px 0,1200px 437px,548px 437px)}
.ind-title{left:79px;top:1152px;font-family:"Arimo",sans-serif;font-size:38px;color:var(--white)}
.ind-text{left:79px;top:1215px;width:490px;font-size:14.5px;line-height:26px;color:var(--white)}
.ind-item{font-size:20px;font-weight:600;color:var(--white);display:flex;align-items:center;gap:13px}
.ind-item::before{content:"";width:10px;height:10px;border-radius:50%;background:var(--white);box-shadow:0 0 0 2px var(--blue),0 0 0 4px var(--white)}
/* services */
.svc-photo{width:229px;height:208px}
.svc h3{font-family:"Raleway",sans-serif;font-weight:500;font-size:25px;color:var(--head);margin-bottom:12px}
.svc p{font-size:14.5px;line-height:26px;margin-bottom:16px}
.svc a{color:var(--link);font-weight:600;font-size:15px;text-decoration:underline}
.svc{width:245px}
/* contact */
.contact{left:0;top:2187px;width:1200px;height:449px;background:var(--panel)}
.contact-title{font-family:"Raleway",sans-serif;font-weight:600;font-size:38px;color:var(--head);text-align:center;width:1200px;left:0;top:2244px}
.field{background:var(--white);border:1px solid #e2e2e2;font-size:14px;color:#777;padding:23px 12px}
/* footer */
.footer{left:0;top:2636px;width:1200px;height:146px;background:var(--footer)}
.footer-bottom{left:0;top:2782px;width:1200px;height:83px;background:var(--footer-bottom);color:var(--white);font-size:14px;display:flex;align-items:center;justify-content:center}
.footer-bottom b{font-weight:600;margin:0 4px}
.footer-links{left:298px;top:2707px;color:var(--white);font-size:15px;white-space:nowrap}
.footer-links i{font-style:normal;margin:0 12px}
.social{width:46px;height:46px;border-radius:50%;background:var(--white)}
</style>
</head>
<body>
<div class="abs hero" role="img" aria-label="Close-up of a CNC lathe turret with a blue coolant hose"></div>
<header class="abs site-header"></header>
<div class="abs brand" style="left:77px;top:38px"><span class="brand-dot"></span>CORVEL RIDGE</div>
<nav class="abs nav">
  <span class="active" style="left:419px">Home</span>
  <span style="left:498px">Services</span>
  <span style="left:593px">Equipment</span>
  <span style="left:702px">Quality</span>
  <span style="left:790px">Our work</span>
  <span style="left:894px">About us</span>
  <span style="left:993px">Contact us</span>
</nav>
<svg class="abs caret" width="14" height="13" viewBox="0 0 14 13"><path d="M7 1 L13 12 H1 Z" fill="none" stroke="#fff" stroke-width="1.3"/></svg>
<svg class="abs search" width="22" height="22" viewBox="0 0 22 22"><circle cx="9" cy="9" r="7" fill="none" stroke="#fff" stroke-width="1.8"/><path d="M14 14 L20 20" stroke="#fff" stroke-width="1.8"/></svg>
<div class="abs hero-box"><h1>From blue print to<br>reality - better than<br>you expected</h1></div>

<h2 class="abs section-title" style="top:736px">WELCOME TO CORVEL RIDGE</h2>
<p class="abs welcome-text">Founded in 1996, Corvel Ridge Machining Inc. was established at the hands of engineering experts, trying to develop a high quality solution for the machining industry.&nbsp; Corvel Ridge Machining Inc. utilizes state of the art, fully automated, equipment.&nbsp; This enables us to provide quick turnaround times, without compromising the quality of the product. We prides ourselves on our friendly and efficient customer service, making sure we meet the needs and standards of our valuable customers. With a knowledgeable team, we provide companies with invaluable support.</p>
<div class="abs btn" style="left:525px;top:979px">Read More</div>

<section class="abs industries"></section>
<div class="abs industries-photo" role="img" aria-label="Machinist inspecting a part at a vertical milling machine"></div>
<h2 class="abs ind-title">INDUSTRIES SERVED</h2>
<p class="abs ind-text">Corvel Ridge Machining Company is a high quality machining resource providing friendly service, fast turnaround times, and engineering expertise, at competitive pricing.</p>
<div class="abs ind-item" style="left:78px;top:1318px">Aerospace</div>
<div class="abs ind-item" style="left:78px;top:1360px">Automotive</div>
<div class="abs ind-item" style="left:78px;top:1402px">Computer</div>
<div class="abs ind-item" style="left:78px;top:1444px">Dental</div>
<div class="abs ind-item" style="left:289px;top:1318px">Electronics</div>
<div class="abs ind-item" style="left:289px;top:1360px">Marine</div>
<div class="abs ind-item" style="left:289px;top:1402px">Medical</div>

<h2 class="abs section-title" style="top:1589px">WHAT WE DO</h2>
<div class="abs svc-photo" style="left:77px;top:1667px;background:linear-gradient(135deg,#d7dadd,#9aa3ad 55%,#b8433c)" role="img" aria-label="Worker operating a CNC machine"></div>
<div class="abs svc" style="left:339px;top:1662px"><h3>Our Service</h3><p>Providing you with honest straightforward service is our number one goal.We manufacture finished metal and plastic goods to tight tolerances</p><a>Read More</a></div>
<div class="abs svc-photo" style="left:613px;top:1667px;background:linear-gradient(180deg,#8a8f95,#c9ccd0 55%,#b5b2ab)" role="img" aria-label="Factory floor with rows of machines"></div>
<div class="abs svc" style="left:875px;top:1662px"><h3>Equipments</h3><p>Toravel Kessin 7 plus axis machining at its best.&nbsp; We offer a diverse fleet of late model Kessin CNC Swiss automatics featuring K-20's,&nbsp; K-32 &amp; R-32's complete.</p><a>Read More</a></div>
<div class="abs svc-photo" style="left:77px;top:1916px;background:linear-gradient(135deg,#5a5f66,#a9adb2 50%,#c9a48c 75%,#2c4f9a)" role="img" aria-label="Hands measuring a chuck with calipers"></div>
<div class="abs svc" style="left:339px;top:1912px"><h3>Quality</h3><p>CORVEL RIDGE Machining recogniz es that the disciplines of quality, health and safety and environ mental management are an integral part of its management.</p><a>Read More</a></div>
<div class="abs svc-photo" style="left:613px;top:1916px;background:linear-gradient(135deg,#dfe3e7,#b4bac1 50%,#3f5f9f 80%,#c2473d)" role="img" aria-label="Two workers at CNC machining centers"></div>
<div class="abs svc" style="left:875px;top:1912px"><h3>Our Work</h3><p>Providing you with honest straightforward service is our number one goal.We manufacture finished metal and plastic goods to tight tolerances</p><a>Read More</a></div>

<section class="abs contact"></section>
<h2 class="abs contact-title">Contact Us</h2>
<div class="abs field" style="left:189px;top:2323px;width:259px;height:62px">Name :</div>
<div class="abs field" style="left:470px;top:2323px;width:259px;height:62px">Email :</div>
<div class="abs field" style="left:751px;top:2323px;width:260px;height:62px">Phone :</div>
<div class="abs field" style="left:189px;top:2406px;width:822px;height:94px">Message / Comments :</div>
<div class="abs btn" style="left:525px;top:2521px">Submit Now</div>

<footer class="abs footer"></footer>
<div class="abs brand" style="left:77px;top:2705px"><span class="brand-dot"></span>CORVEL RIDGE</div>
<div class="abs footer-links">Home<i>|</i>Services<i>|</i>Equipments<i>|</i>Quality<i>|</i>Our work<i>|</i>About us<i>|</i>Contact us</div>
<div class="abs social" style="left:920px;top:2695px" aria-label="Social link"></div>
<div class="abs social" style="left:972px;top:2695px" aria-label="Social link"></div>
<div class="abs social" style="left:1024px;top:2695px" aria-label="Social link"></div>
<div class="abs social" style="left:1077px;top:2695px" aria-label="Social link"></div>
<div class="abs footer-bottom">©&nbsp;<b>CORVEL RIDGE MANUFACTURING</b>- All Rights Reserved</div>
</body>
</html>
```